Tallow Crest Business Card

We need a business card designed for a a company called "Tallow Crest". We offer consulting, coaching and training to business leaders and coaches (across the world) using the latest findings in neuroscience, social and emotional intelligence and positive psychology. The final design should communicate the use of brain science to create sustainable relationships.

The card should be doublesided. The logo is attached and names and titles will be provided to the successful designer. Thank you.

Industry/Entity Type

Training

```html
<!DOCTYPE html>
<html lang="en">
<head>
<meta charset="utf-8">
<title>Tallow Crest Business Card</title>
<link href="https://fonts.googleapis.com/css2?family=Barlow:wght@400;700;800&display=swap" rel="stylesheet">
<style>
  :root {
    --backdrop: #e6e3df;
    --card-dark: #1d1d1d;
    --card-light: #f3f4f5;
    --brand-blue: #1b8bc8;
    --ink: #1a1a1a;
    --ink-soft: #3a3a3a;
    --rule: #c9cccf;
    --on-dark: #eeeeee;
  }
  html, body {
    margin: 0;
    width: 1200px;
    height: 879px;
    overflow: hidden;
    background: var(--backdrop);
    font-family: "Barlow", Arial, sans-serif;
  }
  .canvas {
    position: relative;
    width: 1200px;
    height: 879px;
  }
  .card {
    position: absolute;
    top: 280px;
    width: 540px;
    height: 310px;
    box-shadow: 0 8px 24px rgba(0,0,0,0.18);
  }
  .card--back {
    left: 45px;
    background: var(--card-dark);
    display: flex;
    align-items: center;
    justify-content: center;
  }
  .card--front {
    left: 615px;
    background: var(--card-light);
  }
  .wordmark {
    display: flex;
    align-items: center;
    gap: 12px;
    font-weight: 800;
    letter-spacing: 0.02em;
  }
  .wordmark__dot {
    border-radius: 50%;
    flex: none;
  }
  .card--back .wordmark {
    color: var(--on-dark);
    font-size: 44px;
  }
  .card--back .wordmark__dot {
    width: 22px;
    height: 22px;
    background: var(--on-dark);
  }
  .card--front .wordmark {
    position: absolute;
    left: 34px;
    top: 60px;
    color: var(--brand-blue);
    font-size: 32px;
  }
  .card--front .wordmark__dot {
    width: 16px;
    height: 16px;
    background: var(--brand-blue);
  }
  .person {
    position: absolute;
    right: 34px;
    top: 128px;
    text-align: right;
  }
  .person__name {
    margin: 0;
    font-size: 27px;
    font-weight: 800;
    color: var(--ink);
    line-height: 1;
  }
  .person__surname { color: var(--brand-blue); }
  .person__role {
    margin: 4px 0 0;
    font-size: 13px;
    color: var(--ink-soft);
  }
  .rule {
    position: absolute;
    right: 34px;
    width: 190px;
    height: 1px;
    background: var(--rule);
  }
  .rule--top { top: 186px; }
  .rule--mid { top: 256px; }
  .contact {
    position: absolute;
    right: 34px;
    margin: 0;
    padding: 0;
    list-style: none;
    font-size: 12.5px;
    color: var(--ink-soft);
    text-align: right;
  }
  .contact--lines { top: 192px; }
  .contact--address { top: 262px; }
  .contact__item {
    display: flex;
    justify-content: flex-end;
    align-items: center;
    gap: 8px;
    line-height: 15.5px;
  }
  .contact__icon {
    width: 11px;
    height: 11px;
    fill: var(--brand-blue);
    flex: none;
  }
  .contact__spacer { width: 11px; flex: none; }
</style>
</head>
<body>
<main class="canvas">
  <section class="card card--back" aria-label="Card back">
    <div class="wordmark"><span class="wordmark__dot"></span>Tallow Crest</div>
  </section>

  <section class="card card--front" aria-label="Card front">
    <div class="wordmark"><span class="wordmark__dot"></span>Tallow Crest</div>

    <div class="person">
      <p class="person__name">Name <span class="person__surname">Surname</span></p>
      <p class="person__role">Consultant</p>
    </div>

    <div class="rule rule--top"></div>
    <ul class="contact contact--lines">
      <li class="contact__item">(+00) 123 456 789
        <svg class="contact__icon" viewBox="0 0 12 12"><rect x="3" y="0.5" width="6" height="11" rx="1"/></svg></li>
      <li class="contact__item">(+00) 123 456 789
        <svg class="contact__icon" viewBox="0 0 12 12"><rect x="2" y="1" width="8" height="3"/><rect x="0.5" y="4.5" width="11" height="5" rx="1"/><rect x="3" y="8" width="6" height="3"/></svg></li>
      <li class="contact__item">office@tallowcrest.com
        <svg class="contact__icon" viewBox="0 0 12 12"><path d="M0.5 2.5h11v7h-11z M1 3l5 3.5 5-3.5" fill="var(--brand-blue)"/></svg></li>
      <li class="contact__item">www.tallowcrest.com
        <svg class="contact__icon" viewBox="0 0 12 12"><circle cx="6" cy="6" r="5.5"/><path d="M0.5 6h11M6 0.5v11" stroke="var(--card-light)" stroke-width="0.9"/></svg></li>
    </ul>

    <div class="rule rule--mid"></div>
    <ul class="contact contact--address">
      <li class="contact__item">Your Address Goes Here<span class="contact__spacer"></span></li>
      <li class="contact__item">City, Country, Zipcode
        <svg class="contact__icon" viewBox="0 0 12 12"><path d="M6 0.5a4 4 0 0 1 4 4c0 3-4 7-4 7s-4-4-4-7a4 4 0 0 1 4-4z"/><circle cx="6" cy="4.5" r="1.5" fill="var(--card-light)"/></svg></li>
    </ul>
  </section>
</main>
</body>
</html>
```